Lumo Brew Premium Matcha brand Label

This is a label design project for a luxury tea brand. Feel free to be creative within the guidelines.
Attached to this project is a document called “Private Label Design Requirements” with the design guidelines and template. There is another document called "Lumo Brew Packaging Instructions" this has more details necessary to stick to the guidelines in the first document.

I have also attached the certifications to be included as well as different variations of the logo for you to use.

If you have any questions, I am here.
Updates

Target Market(s)

Young, active, fun, enjoy the finer things

```html
<!DOCTYPE html>
<html lang="en">
<head>
<meta charset="utf-8">
<title>Lumo Brew Premium Matcha Label</title>
<link rel="stylesheet" href="https://fonts.googleapis.com/css2?family=Barlow+Semi+Condensed:wght@400;600;700&display=swap">
<style>
  :root {
    --page: #ffffff;
    --leaf-deep: #4fa72f;
    --leaf-mid: #7cc24a;
    --leaf-pale: #dcedaa;
    --mist: #eef6d2;
    --ink: #1c2616;
    --ink-green: #24501a;
    --badge-green: #3f8a2a;
    --badge-white: #f5f9ee;
  }
  * { margin: 0; padding: 0; box-sizing: border-box; }
  html, body { width: 1200px; height: 254px; overflow: hidden; background: var(--page); }
  body { font-family: "Barlow Semi Condensed", "Arial Narrow", sans-serif; color: var(--ink); position: relative; }

  .label {
    position: absolute; left: 53px; top: 45px; width: 1099px; height: 184px; overflow: hidden;
    background: linear-gradient(90deg, var(--leaf-deep) 0%, var(--leaf-mid) 22%, var(--leaf-pale) 42%, var(--mist) 52%, var(--leaf-pale) 62%, var(--leaf-mid) 80%, var(--leaf-deep) 100%);
  }
  .label-waves { position: absolute; inset: 0; width: 100%; height: 100%; }

  .brand { position: absolute; display: flex; align-items: center; gap: 8px; font-weight: 700; }
  .brand-dot { display: block; border-radius: 50%; background: var(--ink); }
  .brand--side { left: 48px; top: 78px; font-size: 15px; }
  .brand--side .brand-dot { width: 10px; height: 10px; }
  .brand--center { left: 0; right: 0; top: 96px; justify-content: center; font-size: 22px; }
  .brand--center .brand-dot { width: 12px; height: 12px; }

  .origin { position: absolute; left: 50px; top: 108px; font-size: 13.5px; line-height: 17px; }
  .origin-title { font-weight: 700; font-size: 14px; }

  .product { position: absolute; left: 0; right: 0; top: 128px; text-align: center; }
  .product-name { font-weight: 700; font-size: 18px; color: var(--ink-green); line-height: 22px; }
  .product-weight { font-size: 14px; line-height: 18px; }

  .directions { position: absolute; left: 833px; top: 22px; font-size: 13px; line-height: 17.5px; }
  .directions-title { font-weight: 700; font-size: 12.5px; }
  .directions ul { list-style: none; }
  .directions li::before { content: "· "; }

  .certs { position: absolute; left: 841px; top: 129px; display: flex; align-items: center; gap: 10px; }
  .cert { width: 28px; height: 28px; background: var(--badge-white); border: 2px solid var(--badge-green); }
  .cert--round { border-radius: 50%; }
  .storage { margin-left: 6px; font-weight: 700; font-size: 13px; line-height: 14px; color: var(--ink-green); }
</style>
</head>
<body>
  <section class="label">
    <svg class="label-waves" viewBox="0 0 1099 184" preserveAspectRatio="none" role="img" aria-label="Soft flowing green waves with drifting tea leaves">
      <path d="M0 140 C180 60 320 200 520 90 S840 20 1099 110 L1099 184 L0 184 Z" fill="#ffffff" opacity="0.12"/>
      <path d="M0 40 C200 120 380 -10 560 70 S900 150 1099 50" fill="none" stroke="#ffffff" stroke-width="26" opacity="0.14"/>
      <path d="M300 184 C420 110 520 160 640 60 S800 10 900 0" fill="none" stroke="#ffffff" stroke-width="40" opacity="0.12"/>
    </svg>

    <div class="brand brand--side"><span class="brand-dot"></span>Lumo Brew</div>
    <div class="origin">
      <p class="origin-title">Product of Japan</p>
      <p>Distributed by Lumo Brew Co. | Riverton, Ga</p>
      <p>Certified Organic by Verdan</p>
    </div>

    <div class="brand brand--center"><span class="brand-dot"></span>Lumo Brew</div>
    <div class="product">
      <p class="product-name">Premium Organic Ceremonial Matcha</p>
      <p class="product-weight">Net Wt: 30g</p>
    </div>

    <div class="directions">
      <p class="directions-title">Premium Organic Japanese Matcha Green Tea</p>
      <p>Instructions:</p>
      <ul>
        <li>2 tsp of Matcha</li>
        <li>2oz of Water (170-180 degrees F)</li>
        <li>Whisk in a W formation until frothy</li>
        <li>Sweeten to taste</li>
      </ul>
    </div>

    <div class="certs">
      <span class="cert" role="img" aria-label="Non-GMO certification badge"></span>
      <span class="cert cert--round" role="img" aria-label="Organic certification badge"></span>
      <p class="storage">KEEP REFRIGERATED<br>FOR QUALITY</p>
    </div>
  </section>
</body>
</html>
```